Maison Orélie is a premium domestic placement company and a concept of modern etiquette and a manueri

Maison Orélie is a premium domestic placements agency delivering the most professional caliber of domestic professionals to suit even the most demanding, challenging and refined household tasks.

Based in Dubai, Maison Orélie the world of Maison Orélie is representing the finest.

We genuinely strive to find the best, recruit the right ones and invest our time and resources for that perfect match.

~ Career Nannies ~
~ Etiquette Governesses ~
~ Royal Protocol Attendees ~
~ Formal Palace Personnel ~
~ Official Butler ~
~ World Class Chefs ~
~ Skilled Housekeepers ~
~ Experienced Babynurses ~
~ Domestic Couples ~
~ Professional Laundresses ~
~ Personal Beautician ~
~ Enthusiastic Chauffeurs ~
~ Gourmet Cooks ~

WEB SITE BRIEF:

Style: clean, classy, refined and screaming luxury - you may see sample i like: www.lunabrevanhouse.example

Colors: I like black and white with a touch of pink (burned sugar more specifically)

Communicate: The images and the web should communicate class and royalty as i will be working with lots of royal families in the Region.

Images selection: this is very important to me has to be with white, black, and perhaps a touch of pink - just to get along with my logo second line.
1. one image may be a palace
2. may be a housekeeper or a butler
3. something etiquette related! or your
PS. Do not limit to those, its just mine idea and also i don't know why but i prefer images without faces - otherwise looks like endorsement and strong personalization to a face that i dont even know

Note: The pictures i have attached are tentative only

Explanation of my web structure: 1 excel page are the web links 2 are the side links, i want them to be like a sliding tips, that you click to see the next 3 social media i will start with

Standards: You may use my logo (middle icon) as a graphic idea and/or whatever you decide i like consistency - in the colors you use, style and all.

General: Easy to navigate

Thank you all in advance & Enjoy the journey

Marguerite

Target Market(s)

- Royal families and VIP's in Middle East
- Families and families with kids
- Mid and High-end segment singles
- Hotels HR departments
- Companies HR departments
- Celebrities ;)

Industry/Entity Type

It Company

Requirements
Must have
• Standards again of design, i don't like mixed style of photography and drawing and sketches all in one. Think there should be an idea in the backbone
Nice to have
• Clean, i like simple things in life
• Elegant and luxury, reliability and care - that should be the message
• on the MAIN side might have one banner that shows my value added package VIP Maison Orélie consisted of the following:
• - priority served contract
• - draw from the best candidates
• - dedicated consultant
• - FREE couture uniform
• - meeting at your choice
• - FREE training from the Maison Orélie advanced manual
• - FREE cooking book
• - Follow up visit/call
Should not have
• 1. variety of styles as said
• 2. images that are used from others in the same industry and styles
• 3. very big letters - prefer smaller fonts
• 4. illustrations that look cheap

```html
<!DOCTYPE html>
<html lang="en">
<head>
<meta charset="utf-8">
<title>Maison Orélie – Premium Domestic</title>
<link rel="stylesheet" href="https://fonts.googleapis.com/css2?family=Lato:wght@400;700&family=Roboto+Condensed:wght@300;400;700&display=swap">
<style>
  :root{
    --bar:#2c2c30;
    --footer:#45454f;
    --ink:#2a2a2a;
    --muted:#555;
    --pink:#e24b7f;
    --rule:#c9c9c9;
    --card:#f3f3f3;
    --white:#fff;
  }
  *{box-sizing:border-box;margin:0;padding:0}
  html,body{width:924px;height:1200px;overflow:hidden;background:var(--white)}
  body{position:relative;font-family:"Lato",sans-serif;color:var(--ink)}
  .abs{position:absolute}

  .topbar{left:0;top:0;width:924px;height:27px;background:var(--bar);color:var(--white);font-size:13px;display:flex;align-items:center;padding:0 40px}
  .topbar .contact{display:flex;gap:22px;align-items:center}
  .topbar .contact span{display:flex;align-items:center;gap:6px}
  .topbar .account{margin-left:auto;font-size:11px;display:flex;gap:8px}
  .topbar .account i{font-style:normal;opacity:.7}

  .hero{left:23px;top:27px;width:881px;height:442px;border:1px solid #9a9a9a;border-top:none;overflow:hidden;background:var(--white)}
  .hero-photo{left:312px;top:0;width:569px;height:442px;background:linear-gradient(100deg,#fbfaf8 0%,#efe9e2 30%,#e4ddd6 55%,#8c2b49 80%,#f4f2f0 100%)}
  .hero-fade{left:0;top:0;width:460px;height:442px;background:linear-gradient(90deg,#fff 60%,rgba(255,255,255,0))}

  .brand{left:10px;top:10px;width:250px;text-align:center}
  .brand-mark{width:46px;height:46px;border-radius:50%;border:2px solid #222;margin:0 auto 8px}
  .brand-name{font-family:"Lato",sans-serif;font-size:25px;font-weight:700;color:#1e1e1e;letter-spacing:.5px}
  .brand-tag{font-size:8px;letter-spacing:2px;color:var(--pink);margin-top:12px}

  .mainnav{left:34px;top:144px;width:195px;list-style:none}
  .mainnav li{height:31.5px;display:flex;align-items:center;font-size:12px;color:#222;background:linear-gradient(90deg,rgba(0,0,0,0),#d8d8d8 40%,rgba(0,0,0,0)) bottom/100% 1px no-repeat}
  .mainnav li.current{color:var(--pink)}

  .slider-arrow{top:568px;width:18px;height:18px;background:#111;display:flex;align-items:center;justify-content:center}
  .values{top:497px;left:64px;width:806px;display:flex;gap:16px}
  .value-card{width:190px;height:160px;background:var(--card);box-shadow:1px 2px 4px rgba(0,0,0,.35);text-align:center;padding-top:10px}
  .value-card svg{display:block;margin:0 auto}
  .value-card h3{font-family:"Roboto Condensed",sans-serif;font-weight:400;font-size:18px;margin:10px 0 8px;color:#111}
  .value-card p{font-size:11.5px;line-height:16px;text-align:left;padding:0 10px;color:#333}

  .philosophy{left:32px;top:686px;width:571px}
  .section-title{font-family:"Roboto Condensed",sans-serif;font-weight:300;font-size:26px;color:#444}
  .zigzag{margin:6px 0 10px;height:4px;background:repeating-linear-gradient(135deg,#999 0 1px,transparent 1px 3px)}
  .philosophy p{font-size:11.8px;line-height:16px;margin-bottom:14px;color:#222}

  .photo-tile{border:1px solid #888;padding:2px;background:#eee}
  .photo-fill{width:100%;height:100%;position:relative}
  .photo-caption{position:absolute;left:0;right:0;bottom:0;height:24px;background:#1e1e1e;color:var(--white);font-size:13px;display:flex;align-items:center;justify-content:center;letter-spacing:.3px}

  .signup{left:31px;top:963px;width:374px;height:165px;background:#f2f2f2;border:1px solid #ddd}
  .signup h2{font-family:"Roboto Condensed",sans-serif;font-weight:400;font-size:21px;color:#333;padding:11px 11px 9px;border-bottom:1px solid #ddd}
  .signup p{font-size:12px;line-height:16px;padding:8px 7px;color:#222}
  .signup-form{display:flex;gap:10px;padding:12px 6px}
  .signup-form .field{width:256px;height:26px;border:1px solid #aaa;border-radius:3px;background:#fff;font-size:12px;color:#444;display:flex;align-items:center;padding-left:8px}
  .signup-form .button{height:24px;margin-top:1px;padding:0 8px;background:#151515;color:#fff;border-radius:3px;font-size:12px;display:flex;align-items:center;gap:6px}

  .footer{left:22px;top:1165px;width:882px;height:35px;background:var(--footer);color:#eee;font-size:11px;display:flex;align-items:center;padding:0 26px}
  .social{margin-left:auto;display:flex;gap:12px}
  .social span{width:25px;height:25px;border-radius:50%;background:#f2f2f2;border:2px solid #cfd3da;display:block}
</style>
</head>
<body>

<header class="abs topbar">
  <div class="contact">
    <span><svg width="12" height="9" viewBox="0 0 12 9"><rect width="12" height="9" fill="#fff"/><path d="M0 0l6 5 6-5" stroke="#2c2c30" fill="none"/></svg>info@maisonorelie.example</span>
    <span><svg width="10" height="12" viewBox="0 0 10 12"><path d="M2 0h2l1 3-1.5 1a6 6 0 003 4l1-1.5 3 1v2c0 1-1 2-2 2C4 11 0 7 0 2 0 1 1 0 2 0z" fill="#fff"/></svg>01632 960 418</span>
    <span><svg width="11" height="11" viewBox="0 0 11 11"><circle cx="5.5" cy="3" r="3" fill="#fff"/><path d="M0 11c0-4 11-4 11 0z" fill="#fff"/></svg>Login</span>
  </div>
  <nav class="account">My Account <i>|</i> Friendsheet <i>|</i> Chirper <i>|</i> Login</nav>
</header>

<section class="abs hero">
  <div class="abs hero-photo" role="img" aria-label="Housekeeper in a burgundy uniform holding folded white towels in a bright bedroom"></div>
  <div class="abs hero-fade"></div>
  <div class="abs brand">
    <div class="brand-mark"></div>
    <div class="brand-name">Maison Orélie</div>
    <div class="brand-tag">PREMIUM DOMESTIC</div>
  </div>
  <ul class="abs mainnav">
    <li class="current">Home</li>
    <li>About</li>
    <li>Clients</li>
    <li>Candidate</li>
    <li>VIP &amp; Royal</li>
    <li>Media</li>
    <li>Partner</li>
    <li>Contact</li>
  </ul>
</section>

<div class="abs slider-arrow" style="left:32px"><svg width="8" height="10"><path d="M7 0L1 5l6 5z" fill="#fff"/></svg></div>
<div class="abs slider-arrow" style="left:878px"><svg width="8" height="10"><path d="M1 0l6 5-6 5z" fill="#fff"/></svg></div>

<section class="abs values">
  <article class="value-card">
    <svg width="28" height="26" viewBox="0 0 28 26"><path d="M14 0L28 26H0z" fill="#555"/><rect x="12.5" y="8" width="3" height="10" fill="#f3f3f3"/><rect x="12.5" y="20" width="3" height="3" fill="#f3f3f3"/></svg>
    <h3>RESPECT</h3>
    <p>At Maison Orélie we care about our fellow human and we do think respecting others .....</p>
  </article>
  <article class="value-card">
    <svg width="28" height="28" viewBox="0 0 28 28"><rect width="28" height="28" rx="3" fill="#555"/><circle cx="20" cy="7" r="3" fill="#f3f3f3"/><circle cx="8" cy="14" r="3" fill="#f3f3f3"/><circle cx="20" cy="21" r="3" fill="#f3f3f3"/><path d="M20 7L8 14l12 7" stroke="#f3f3f3" stroke-width="1.6" fill="none"/></svg>
    <h3>SHARING</h3>
    <p>At Maison Orélie we care about our fellow human and we do think respecting others ....</p>
  </article>
  <article class="value-card">
    <svg width="28" height="28" viewBox="0 0 28 28"><rect width="28" height="28" rx="3" fill="#555"/><rect x="6" y="15" width="3" height="8" fill="#f3f3f3"/><rect x="11" y="9" width="3" height="14" fill="#f3f3f3"/><rect x="16" y="12" width="3" height="11" fill="#f3f3f3"/><rect x="21" y="6" width="3" height="17" fill="#f3f3f3"/></svg>
    <h3>FULLFILLMENT</h3>
    <p>At Maison Orélie we care about our fellow human and we do think respecting others ......</p>
  </article>
  <article class="value-card">
    <svg width="26" height="28" viewBox="0 0 26 28"><circle cx="13" cy="7" r="6" fill="#555"/><path d="M1 28c0-11 24-11 24 0z" fill="#555"/></svg>
    <h3>HUMAN DIGNITY</h3>
    <p>At Maison Orélie we value the people for who they are, coming from each and every part ....</p>
  </article>
</section>

<section class="abs philosophy">
  <h2 class="section-title">Our Philosophy</h2>
  <div class="zigzag"></div>
  <p>At Maison Orélie, we have a special philosophy of living that is imbedded in what we do and our honest efforts of supporting our industry in setting the standards of household staffing a little bit higher. We have bestowed the name of Maison Orélie not only as a concept, but an attitude towards life and work.</p>
  <p>Maison Orélie is a French name; in terms of its actual meaning, maison means “house” and the name stands for a home well kept. However the concept also encompasses the customs of a good society and breeding, ability to live life well and with intelligent enjoyment, meeting every situation with poise, good manners, and elegance.</p>
  <p>While the definition of a well kept house is rather simple, its meaning is much more romantic and thoughtful. It does not simply mean one knows how to live. Rather, it means one knows how to live well, get the most joy out of life, and live life to the fullest by respecting the inter-cultural differences of life.</p>
</section>

<div class="abs photo-tile" style="left:624px;top:718px;width:277px;height:184px">
  <div class="photo-fill" role="img" aria-label="Butler standing behind a formally set dining table with flowers and candelabra" style="background:linear-gradient(180deg,#d9d6d0 0%,#3a2e28 40%,#a4492e 70%,#4c3a22 100%)">
    <div class="photo-caption">EVERYDAY ETIQUETTES &amp; COURTESIES</div>
  </div>
</div>

<section class="abs signup">
  <h2>Sign Up For Job Alerts</h2>
  <p>Get daily, weekly or monthly job alerts by registering with Brightwell. You’ll be kept up-to-date with the latest hot jobs in your speciality.</p>
  <div class="signup-form">
    <div class="field">Type your email id here</div>
    <div class="button">Register <svg width="6" height="9"><path d="M1 0l4 4.5L1 9" stroke="#fff" stroke-width="2" fill="none"/></svg></div>
  </div>
</section>

<div class="abs photo-tile" style="left:424px;top:964px;width:230px;height:165px">
  <div class="photo-fill" role="img" aria-label="Elegant table setting with glassware, napkins and a floral centrepiece" style="background:linear-gradient(180deg,#c9c2b0 0%,#6c6250 45%,#e6e3dc 75%,#b7b0a2 100%)">
    <div class="photo-caption">TABLE SITTING ETIQUETTES</div>
  </div>
</div>

<div class="abs photo-tile" style="left:668px;top:964px;width:230px;height:165px">
  <div class="photo-fill" role="img" aria-label="Child learning table manners with a parent at a breakfast table" style="background:linear-gradient(135deg,#d8c7a6 0%,#b99d78 40%,#f1ece4 70%,#cfd6df 100%)">
    <div class="photo-caption">ETIQUETTES FOR KIDS</div>
  </div>
</div>

<footer class="abs footer">
  © 2013, All Rights Reserved, Maison Orélie
  <div class="social"><span></span><span></span><span></span></div>
</footer>

</body>
</html>
```